Vexora app design refresh: 1 new screen, 1 new icon / 11 icons reworked for hi-res, addtnl elements

UPDATE: added task 6

I have a ready design for the app that needs to be updated, but my previous designer can't help due to the workload.

Tasks which need to be accomplished:
1) new Tutorial icon - we used question mark in a
circle for Tutorial request, but I need something different now, because Tutorials are more about assistance than help in a traditional sense; I am thinking about pencil or graduation hat icons, but am open to other ideas
2) guidance on control elements: when you first open Journal screen you should see the bubble around the '+' icon with the text 'Start Here' inside - I need this bubble with text (shape, color etc.)
3) new Tutorial screen - half-transparent dark layer over the screen, where you see the name of the step than some formatted text plus Populate and Continue buttons at the bottom
4) the icons should be reworked for high resolution screens (6 and 6+) - including keyboard, letter A, icons inside the text formatting panel, tag, export, delete (especially keyboard icon)
5) I want one more color introduced for text - now we have only white and black/grey; for example I want the title of the step look different from the text, different color; so, just give me another color which would look great with existing palette
6) Icon for Summary functionality needs to be created; Archive with appropriate themes is attached

Attached is the existing design for Quorin 4s. Your target design should be for 4s and 5/5s and 6/6+

• 4/4s/5/5s/6/6+ quality

```html
<!DOCTYPE html>
<html lang="en">
<head>
<meta charset="utf-8">
<title>Tutorial Screen – Colour Variations</title>
<link href="https://fonts.googleapis.com/css2?family=Roboto:wght@300;400;500;700&display=swap" rel="stylesheet">
<style>
  :root {
    --canvas: #ffffff;
    --banner: #ff8f84;
    --banner-text: #ffffff;
    --label: #666666;
    --note: #707070;
    --accent-teal: #4fc4aa;
    --body-text: #ffffff;
    --status-text: #ffffff;

    --cold-bg: #21323f;
    --cold-bar: #132b37;
    --cold-ghost: #2a3f4d;
    --cold-populate: #7f8084;
    --cold-continue: #5aa698;

    --warm-bg: #383434;
    --warm-bar: #2a2c2a;
    --warm-ghost: #454140;
    --warm-populate: #03aef0;
    --warm-continue: #fd8a7f;

    --deep-bg: #2f4a42;
    --deep-bar: #1c3d33;
    --deep-ghost: #3a574e;
    --deep-populate: #5aa898;
    --deep-continue: #4fc4aa;
  }
  * { box-sizing: border-box; margin: 0; padding: 0; }
  html, body {
    width: 1200px; height: 999px; overflow: hidden;
    background: var(--canvas);
    font-family: "Roboto", sans-serif;
  }
  .board { position: relative; width: 1200px; height: 999px; }

  .banner {
    position: absolute; left: 0; top: 33px; width: 1200px; height: 62px;
    background: var(--banner);
  }
  .banner-title {
    position: absolute; left: 0; width: 1170px; top: 8px;
    text-align: center; color: var(--banner-text);
    font-weight: 500; font-size: 41px; letter-spacing: 0.3px; line-height: 48px;
  }

  .variant-label {
    position: absolute; width: 400px; margin-left: -200px;
    text-align: center; color: var(--label); font-weight: 300;
  }
  .variant-label .version { font-size: 40px; line-height: 40px; position: absolute; top: 180px; width: 100%; }
  .variant-label .mood { font-size: 20px; line-height: 24px; position: absolute; top: 223px; width: 100%; }

  .phone {
    position: absolute; top: 307px; width: 315px; height: 559px;
    background: var(--bg);
    box-shadow: 0 0 10px rgba(0,0,0,0.28);
    overflow: hidden;
  }
  .phone.cold { left: 67px; --bg: var(--cold-bg); --bar: var(--cold-bar); --ghost: var(--cold-ghost); --populate: var(--cold-populate); --continue: var(--cold-continue); }
  .phone.warm { left: 441px; --bg: var(--warm-bg); --bar: var(--warm-bar); --ghost: var(--warm-ghost); --populate: var(--warm-populate); --continue: var(--warm-continue); }
  .phone.deep { left: 816px; --bg: var(--deep-bg); --bar: var(--deep-bar); --ghost: var(--deep-ghost); --populate: var(--deep-populate); --continue: var(--deep-continue); }

  .app-bar { position: absolute; left: 0; top: 0; width: 100%; height: 43px; background: var(--bar); }
  .status-bar {
    position: absolute; left: 0; top: 0; width: 100%; height: 20px;
    color: var(--status-text); font-size: 11.5px; line-height: 20px;
  }
  .status-bar .carrier { position: absolute; left: 4px; display: flex; align-items: center; gap: 3px; }
  .status-bar .time { position: absolute; left: 0; width: 100%; text-align: center; font-weight: 500; }
  .status-bar .battery { position: absolute; right: 6px; display: flex; align-items: center; gap: 4px; }
  .app-name {
    position: absolute; top: 19px; left: 0; width: 100%; text-align: center;
    color: var(--ghost); font-size: 16px; font-weight: 500; line-height: 20px;
  }

  .ghost-title {
    position: absolute; top: 76px; left: 0; width: 100%; text-align: center;
    color: var(--ghost); font-size: 18px; font-weight: 400;
  }
  .ghost-note {
    position: absolute; top: 378px; left: 35px; width: 245px; text-align: center;
    color: var(--ghost); font-size: 9.5px; line-height: 12px; font-weight: 300;
  }

  .step-title {
    position: absolute; top: 86px; left: 0; width: 100%; text-align: center;
    color: var(--accent-teal); font-size: 36px; font-weight: 300; line-height: 44px;
  }
  .step-body {
    position: absolute; top: 145px; left: 35px; width: 245px;
    color: var(--body-text); font-size: 15px; font-weight: 300; line-height: 19.25px;
  }
  .step-body span { display: block; text-align: justify; text-align-last: justify; white-space: nowrap; }
  .step-body span.last { text-align-last: left; }

  .actions { position: absolute; top: 466px; left: 35px; width: 245px; height: 31px; }
  .btn {
    position: absolute; top: 0; width: 114px; height: 31px; border-radius: 2px;
    color: #fff; font-size: 13px; font-weight: 400; line-height: 31px; text-align: center;
    text-transform: uppercase;
  }
  .btn.populate { left: 0; background: var(--populate); }
  .btn.continue { left: 131px; background: var(--continue); }

  .notes {
    position: absolute; left: 67px; top: 893px;
    color: var(--note); font-size: 19px; font-weight: 300; line-height: 24.5px;
  }
</style>
</head>
<body>
<div class="board">
  <header class="banner"><h1 class="banner-title">#3 - Tutorial Screen</h1></header>

  <div class="variant-label" style="left:210px"><div class="version">v1</div><div class="mood">cold</div></div>
  <div class="variant-label" style="left:593px"><div class="version">v2</div><div class="mood">warm</div></div>
  <div class="variant-label" style="left:974px"><div class="version">v3</div><div class="mood">app’s main color, but much darker</div></div>

  <!-- phone screens -->
  <section class="phone cold">
    <div class="app-bar"></div>
    <div class="status-bar">
      <div class="carrier">●●●○○ Carrier
        <svg width="12" height="9" viewBox="0 0 12 9"><path d="M6 9 L3.6 6.3 A3.4 3.4 0 0 1 8.4 6.3 Z M1.8 4.4 A6 6 0 0 1 10.2 4.4 L9.2 5.4 A4.6 4.6 0 0 0 2.8 5.4 Z M0 2.5 A8.6 8.6 0 0 1 12 2.5 L11 3.5 A7.2 7.2 0 0 0 1 3.5 Z" fill="#fff"/></svg>
      </div>
      <div class="time">8:08 AM</div>
      <div class="battery">50%
        <svg width="24" height="10" viewBox="0 0 24 10"><rect x="0.5" y="0.5" width="21" height="9" rx="1.5" fill="none" stroke="#fff"/><rect x="2" y="2" width="10" height="6" fill="#fff"/><rect x="22" y="3" width="1.5" height="4" fill="#fff"/></svg>
      </div>
    </div>
    <div class="app-name">Vexora</div>
    <div class="ghost-title">Activating Event</div>
    <div class="ghost-note">Describe the moment that triggered your reaction in a few words<br>tap plus to add more</div>
    <h2 class="step-title">Step 1</h2>
    <div class="step-body">
      <span>Lorem ipsum dolor sit amet, con-</span>
      <span>sectetur adipisicing elit, sed do eius-</span>
      <span>mod tempor incididunt ut labore et</span>
      <span>dolore magna aliqua. Ut enim ad</span>
      <span>minim veniam, quis nostrud exerci-</span>
      <span>tation ullamco laboris nisi ut aliquip</span>
      <span>ex ea commodo consequat. Duis</span>
      <span>aute irure dolor in reprehenderit in</span>
      <span>voluptate velit esse cillum dolore eu</span>
      <span>fugiat nulla pariatur. Excepteur sint</span>
      <span>occaecat cupidatat non proident,</span>
      <span>sunt in culpa qui officia deserunt</span>
      <span class="last">mollit anim id est laborum.</span>
    </div>
    <div class="actions"><div class="btn populate">Populate</div><div class="btn continue">Continue</div></div>
  </section>

  <section class="phone warm">
    <div class="app-bar"></div>
    <div class="status-bar">
      <div class="carrier">●●●○○ Carrier
        <svg width="12" height="9" viewBox="0 0 12 9"><path d="M6 9 L3.6 6.3 A3.4 3.4 0 0 1 8.4 6.3 Z M1.8 4.4 A6 6 0 0 1 10.2 4.4 L9.2 5.4 A4.6 4.6 0 0 0 2.8 5.4 Z M0 2.5 A8.6 8.6 0 0 1 12 2.5 L11 3.5 A7.2 7.2 0 0 0 1 3.5 Z" fill="#fff"/></svg>
      </div>
      <div class="time">8:08 AM</div>
      <div class="battery">50%
        <svg width="24" height="10" viewBox="0 0 24 10"><rect x="0.5" y="0.5" width="21" height="9" rx="1.5" fill="none" stroke="#fff"/><rect x="2" y="2" width="10" height="6" fill="#fff"/><rect x="22" y="3" width="1.5" height="4" fill="#fff"/></svg>
      </div>
    </div>
    <div class="app-name">Vexora</div>
    <div class="ghost-title">Activating Event</div>
    <div class="ghost-note">Describe the moment that triggered your reaction in a few words<br>tap plus to add more</div>
    <h2 class="step-title">Step 1</h2>
    <div class="step-body">
      <span>Lorem ipsum dolor sit amet, con-</span>
      <span>sectetur adipisicing elit, sed do eius-</span>
      <span>mod tempor incididunt ut labore et</span>
      <span>dolore magna aliqua. Ut enim ad</span>
      <span>minim veniam, quis nostrud exerci-</span>
      <span>tation ullamco laboris nisi ut aliquip</span>
      <span>ex ea commodo consequat. Duis</span>
      <span>aute irure dolor in reprehenderit in</span>
      <span>voluptate velit esse cillum dolore eu</span>
      <span>fugiat nulla pariatur. Excepteur sint</span>
      <span>occaecat cupidatat non proident,</span>
      <span>sunt in culpa qui officia deserunt</span>
      <span class="last">mollit anim id est laborum.</span>
    </div>
    <div class="actions"><div class="btn populate">Populate</div><div class="btn continue">Continue</div></div>
  </section>

  <section class="phone deep">
    <div class="app-bar"></div>
    <div class="status-bar">
      <div class="carrier">●●●○○ Carrier
        <svg width="12" height="9" viewBox="0 0 12 9"><path d="M6 9 L3.6 6.3 A3.4 3.4 0 0 1 8.4 6.3 Z M1.8 4.4 A6 6 0 0 1 10.2 4.4 L9.2 5.4 A4.6 4.6 0 0 0 2.8 5.4 Z M0 2.5 A8.6 8.6 0 0 1 12 2.5 L11 3.5 A7.2 7.2 0 0 0 1 3.5 Z" fill="#fff"/></svg>
      </div>
      <div class="time">8:08 AM</div>
      <div class="battery">50%
        <svg width="24" height="10" viewBox="0 0 24 10"><rect x="0.5" y="0.5" width="21" height="9" rx="1.5" fill="none" stroke="#fff"/><rect x="2" y="2" width="10" height="6" fill="#fff"/><rect x="22" y="3" width="1.5" height="4" fill="#fff"/></svg>
      </div>
    </div>
    <div class="app-name">Vexora</div>
    <div class="ghost-title">Activating Event</div>
    <div class="ghost-note">Describe the moment that triggered your reaction in a few words<br>tap plus to add more</div>
    <h2 class="step-title">Step 1</h2>
    <div class="step-body">
      <span>Lorem ipsum dolor sit amet, con-</span>
      <span>sectetur adipisicing elit, sed do eius-</span>
      <span>mod tempor incididunt ut labore et</span>
      <span>dolore magna aliqua. Ut enim ad</span>
      <span>minim veniam, quis nostrud exerci-</span>
      <span>tation ullamco laboris nisi ut aliquip</span>
      <span>ex ea commodo consequat. Duis</span>
      <span>aute irure dolor in reprehenderit in</span>
      <span>voluptate velit esse cillum dolore eu</span>
      <span>fugiat nulla pariatur. Excepteur sint</span>
      <span>occaecat cupidatat non proident,</span>
      <span>sunt in culpa qui officia deserunt</span>
      <span class="last">mollit anim id est laborum.</span>
    </div>
    <div class="actions"><div class="btn populate">Populate</div><div class="btn continue">Continue</div></div>
  </section>

  <p class="notes">
    a few different variations of button colors here<br>
    if you wish people to press more often on a specific button it should be much brighter than the other<br>
    if not they both could be the same color
  </p>
</div>
</body>
</html>
```